Artistic eBook Cover - Front only

Create an artistic book cover (front only) for the ebook novel Veil of Ember. Be creative! Use one, or several, of the central images to create an eye-catching professional cover. The cover should be intriguing and make the reader want to know "What is a veil of ember and why do I need it?" Please use a distinctive font/typography that fits the theme of the novel.
The cover should include the following information:
Title: Veil of Ember
Author: Mira Talvane
Company: A QuillFern Creation
The novel has fantasy and science fiction elements. The target reader is between 18 - 38 years old and has interests in international travel, foreign languages, the psychology of symbols, spirituality/female deities, and the healing powers of music.
Description of novel: There is a 6th sense, a veil of ember, that will give us the power to return to paradise and live with the Gods (female deities known as "The Mothers"). The book follows the main characters as they search across the U.S., Brazil, and Ghana in search of a supernatural song that will allow them to tap into their 6th sense.
Main idea of the novel: All humans have precious metal under their skin and inside of them (imagine your bones were made of gold and gem stones). The supernatural song, when heard, will be like a tuning fork striking the metal inside of us and causing a vibration strong enough to shatter all illusions and allowing humans to return to paradise.
Central Images:
1. The rising sun, the rising moon, the ocean.
2. The main character is an African-American woman with 8 long cornrows/braids that hang below her waist
3. The Mothers are a group of women of color (African, Native American, Asian, Latin) who watch over all of humanity like overprotective mothers
4. In one important scene an African man walks up to heaven by walking on the moonlight reflected by the ocean and then walking up the stars as if they are a staircase.
5. A female singer with dredlocks who hides the veil of ember in a small red pouch.
Deliverables:
1. 1600w x 2400h pixel image in jpeg format
2. 300 DPI copy of all assets used in the design
3. 1600w x 2400h 300 DPI layered PhotoShop file of the cover layout
4. A copy of all fonts used in the design (for minor ongoing changes to title or company name)
Designer to choose colors to be used in the design.
Requirements
Must have
- Authors name: Mira Talvane

```html
<!DOCTYPE html>
<html lang="en">
<head>
<meta charset="UTF-8">
<title>Veil of Ember — Mira Talvane</title>
<link rel="stylesheet" href="https://fonts.googleapis.com/css2?family=Cherry+Swash:wght@400;700&display=swap">
<style>
  :root {
    --backdrop: #e4e4e6;
    --ember-deep: #6e0b0a;
    --ember-dark: #8e0f0e;
    --ember-red: #c8201a;
    --ember-orange: #e0621c;
    --sun-gold: #f2a43a;
    --ridge: #a3161a;
    --sea: #d2301f;
    --ink: #1c1412;
    --shadow: rgba(0, 0, 0, 0.28);
  }

  * { margin: 0; padding: 0; box-sizing: border-box; }

  html, body {
    width: 1200px;
    height: 800px;
    overflow: hidden;
  }

  body {
    background: var(--backdrop);
    position: relative;
    font-family: "Cherry Swash", serif;
  }

  .book-cover {
    position: absolute;
    left: 360px;
    top: 40px;
    width: 480px;
    height: 720px;
    overflow: hidden;
    background:
      radial-gradient(circle at 40% 24%, var(--sun-gold) 0%, var(--ember-orange) 16%, rgba(224, 98, 28, 0) 42%),
      radial-gradient(ellipse at 78% 38%, rgba(224, 98, 28, 0.6) 0%, rgba(224, 98, 28, 0) 55%),
      linear-gradient(180deg, var(--ember-red) 0%, #d23a1c 35%, var(--ember-red) 60%, var(--ember-dark) 100%);
    box-shadow: 0 18px 40px var(--shadow);
  }

  .cover-scene {
    position: absolute;
    left: 0;
    right: 0;
    top: 395px;
    bottom: 0;
    background:
      radial-gradient(ellipse 60% 35% at 55% 30%, rgba(240, 80, 40, 0.55) 0%, rgba(240, 80, 40, 0) 100%),
      linear-gradient(180deg,
        rgba(163, 22, 26, 0) 0%,
        var(--ridge) 18%,
        #b81c1c 34%,
        var(--sea) 42%,
        #b51d18 52%,
        var(--ember-dark) 72%,
        var(--ember-deep) 100%);
  }

  .cover-author {
    position: absolute;
    top: 30px;
    left: 0;
    right: 0;
    text-align: center;
    font-size: 30px;
    font-weight: 400;
    color: var(--ink);
    letter-spacing: 0.5px;
  }

  .cover-title {
    position: absolute;
    top: 92px;
    left: 0;
    right: 0;
    text-align: center;
    color: var(--ink);
    font-weight: 400;
    font-size: 90px;
    line-height: 102px;
    letter-spacing: 1px;
    text-transform: uppercase;
  }

  .cover-title span { display: block; }

  .cover-imprint {
    position: absolute;
    bottom: 22px;
    left: 0;
    right: 0;
    text-align: center;
    font-size: 18px;
    font-weight: 400;
    color: var(--sun-gold);
    letter-spacing: 0.5px;
  }
</style>
</head>
<body>
  <main class="book-cover">
    <div class="cover-scene" role="img" aria-label="Silhouette of a woman carrying a small pouch, standing before red mountains and a glowing sea at sunrise"></div>
    <p class="cover-author">Mira Talvane</p>
    <h1 class="cover-title">
      <span>Veil</span>
      <span>of</span>
      <span>Ember</span>
    </h1>
    <p class="cover-imprint">A QuillFern Creation</p>
  </main>
</body>
</html>
```